Recruitment Agency Needs a Core Values Wall for Office

Hello! We are hoping to reach out to the designer community to help us with achieving a wall in our office that beautifully presents our core values, so thanks for stopping by!
We are in a corporate office, but our median age in the office is 28 years old. For this reason we want the design to be fun, young and colourful while showing some sophistication.
The wall will be visible to the staff (within the open plan office), and the right colours will need to be used to enhance mood and productivity. Perhaps we could be looking at a colour for each core value? Or potentially some other way for each value to stand out?
The background doesn't have to be a specific colour. We would like some options to see how it will reflect in the office.
In terms of size - we aren't 100% on what size we are wanting to do it... but work within 1500x2700mm and we can work off that.
Fonts can be experimented with, without being too overpowering to the eye.
It needs to be clear, punchy and stand out from across the office (while being easy on the eye).
I have attached two images that can be used as inspiration. We would like more colour throughout the design.
The core values that will be required to be displayed:
Stop. Think. Challenge the Norm.
Our Detail is Our Difference.
Best Intentions. ALWAYS.
Turn Up, Turn On! Make ..it Happen!
Support Like Family. Party Like Rockstars.
Median staff age of 28, corporate office
Recruitment

```html
<!DOCTYPE html>
<html lang="en">
<head>
<meta charset="utf-8">
<title>Core Values Wall</title>
<link rel="stylesheet" href="https://fonts.googleapis.com/css2?family=Stardos+Stencil:wght@700&family=Michroma&family=Alfa+Slab+One&family=Saira+Stencil+One&family=Lobster&family=Sancreek&display=swap">
<style>
  :root {
    --paper: #f0f0ef;
    --green: #8fb35c;
    --orange: #d8703f;
    --amber: #e8883a;
    --plum: #a55a86;
    --rule: #df8446;
    --rule-dark: #c9663a;
  }
  html, body {
    margin: 0;
    padding: 0;
    width: 881px;
    height: 1200px;
    overflow: hidden;
    background: var(--paper);
  }
  .values-wall {
    display: block;
    width: 881px;
    height: 1200px;
    background: linear-gradient(180deg, #f3f3f2 0%, #ebebea 100%);
  }
  .rule { stroke: var(--rule); stroke-width: 3; }
  .rule--dark { stroke: var(--rule-dark); }
  .stencil { font-family: "Stardos Stencil", "Courier New", serif; font-weight: 700; }
  .wide-sans { font-family: "Michroma", "Arial", sans-serif; }
  .slab { font-family: "Alfa Slab One", "Georgia", serif; }
  .block-stencil { font-family: "Saira Stencil One", "Impact", sans-serif; }
  .script { font-family: "Lobster", "Brush Script MT", cursive; }
  .western { font-family: "Sancreek", "Georgia", serif; }
  .green { fill: var(--green); }
  .orange { fill: var(--orange); }
  .amber { fill: var(--amber); }
  .plum { fill: var(--plum); }
  .icon { fill: var(--amber); }
  .figure { fill: var(--orange); }
</style>
</head>
<body>
<svg class="values-wall" viewBox="0 0 881 1200" xmlns="http://www.w3.org/2000/svg" role="img" aria-label="Core values wall">

  <!-- Value 1 -->
  <line class="rule" x1="138" y1="76" x2="745" y2="76"/>
  <text class="stencil green" x="145" y="161" font-size="96" textLength="627" lengthAdjust="spacingAndGlyphs">STOP. THINK.</text>
  <text class="stencil orange" x="136" y="229" font-size="56" textLength="628" lengthAdjust="spacingAndGlyphs">CHALLENGE THE NORM.</text>

  <line class="rule" x1="124" y1="257" x2="418" y2="257"/>
  <rect class="icon" x="422" y="240" width="34" height="34" rx="6" role="img" aria-label="Thumbs-up icon"/>
  <line class="rule" x1="462" y1="257" x2="755" y2="257"/>

  <!-- Value 2 -->
  <text class="wide-sans green" x="130" y="355" font-size="86" textLength="298" lengthAdjust="spacingAndGlyphs">OUR</text>
  <text class="wide-sans green" x="130" y="390" font-size="30" textLength="293" lengthAdjust="spacingAndGlyphs">DETAIL IS</text>
  <text class="slab orange" x="458" y="390" font-size="140" textLength="293" lengthAdjust="spacingAndGlyphs">OUR</text>
  <text class="slab orange" x="135" y="485" font-size="104" textLength="613" lengthAdjust="spacingAndGlyphs">DIFFERENCE.</text>

  <line class="rule rule--dark" x1="124" y1="515" x2="405" y2="515"/>
  <rect class="figure" x="408" y="506" width="68" height="18" rx="6" role="img" aria-label="Pointing hand icon"/>
  <line class="rule rule--dark" x1="480" y1="515" x2="755" y2="515"/>

  <!-- Value 3 -->
  <rect class="icon" x="63" y="546" width="68" height="18" rx="9" role="img" aria-label="Flourish ornament"/>
  <text class="stencil amber" x="140" y="569" font-size="40" textLength="604" lengthAdjust="spacingAndGlyphs">BEST INTENTIONS. ALWAYS.</text>
  <rect class="icon" x="750" y="546" width="68" height="18" rx="9" role="img" aria-label="Flourish ornament"/>

  <line class="rule rule--dark" x1="124" y1="607" x2="410" y2="607"/>
  <circle class="icon" cx="440" cy="604" r="25" role="img" aria-label="Smiley icon"/>
  <line class="rule rule--dark" x1="470" y1="607" x2="755" y2="607"/>

  <!-- Value 4 -->
  <text class="block-stencil green" x="141" y="695" font-size="58" textLength="602" lengthAdjust="spacingAndGlyphs">TURN UP, TURN ON!</text>
  <text class="block-stencil green" x="141" y="749" font-size="58" textLength="602" lengthAdjust="spacingAndGlyphs">MAKE ..IT HAPPEN!</text>

  <line class="rule" x1="160" y1="783" x2="420" y2="783"/>
  <rect class="icon" x="425" y="764" width="30" height="32" rx="6" role="img" aria-label="Thumbs-up icon"/>
  <line class="rule" x1="460" y1="783" x2="760" y2="783"/>

  <!-- Value 5 -->
  <text class="script plum" x="126" y="848" font-size="60" textLength="632" lengthAdjust="spacingAndGlyphs">Support Like Family.</text>
  <text class="western orange" x="134" y="957" font-size="92" textLength="320" lengthAdjust="spacingAndGlyphs">PARTY</text>
  <rect class="figure" x="463" y="872" width="44" height="130" rx="12" role="img" aria-label="Silhouette of a rockstar with raised arm"/>
  <text class="western orange" x="514" y="957" font-size="92" textLength="234" lengthAdjust="spacingAndGlyphs">LIKE</text>

  <line class="rule rule--dark" x1="126" y1="992" x2="458" y2="992"/>
  <line class="rule rule--dark" x1="512" y1="992" x2="755" y2="992"/>

  <text class="western plum" x="130" y="1105" font-size="106" textLength="660" lengthAdjust="spacingAndGlyphs">ROCKSTARS.</text>

  <line class="rule rule--dark" x1="126" y1="1133" x2="755" y2="1133"/>
</svg>
</body>
</html>
```